2008年から発行を続けている当社唯一の社外報「星空MIDORI帖」の
1面に掲載するタイトル(見出し部分)のデザインを依頼いたします。
(添付参照:現在のタイトル)

〇星空MIDORI帖
・A4 8ページものの新聞
・知財関連のニュースやイベント、当社製品の紹介などを掲載
・年2度(6/11月)発行
・配布は印刷/データ(現在はデータの方が多い)

〇希望イメージ
・これまでの「真面目な」「由緒ある」といった印象だけではなく
「親しみやすさ」や「身近さ」「明るさ」「元気の良さ」「スタイリッシュさ」を伝えられる紙面にしたい
・読者は企業の知財部の方々なので子供っぽいデザインは避けたい
・企業カラーの緑色をベースにしたい

また、選ばせていただいたデザインをご提案いただいたデザイナー様には
続けてサブ見出し(1面以降のすべての紙面 上部中央に掲載する小さなもの)も
依頼させていただきたいと考えております。

以上、どうぞよろしくお願いいたします。
〇タイトル
・1面に掲載
・掲載サイズ:W188mm H76.6㎜
・入れていただきたい事項
①弊社所在地等の情報
第〇号
発行日(例:2022年3月23日)
発行 株式会社青葉書房社
https://www.aobashobo-sample.co.jp/
東京 千代田区外松原3-5-8 TEL:03-4927-6830
大阪 大阪市北区西桜台4-7-21 TEL:06-6718-2945
名古屋 刈谷市若草町5-14-3 TEL:0566-71-2049
②掲載記事のタイトルを記入できるスペース(W50mmH35.2mmほど)
希望イメージ
青系、緑系

弊社の希望する明るさ、爽やかさと知的財産を素敵に融合いただいたと感じました。
ご提案いただいた際の丁寧な文章も決め手の1つでした。

曖昧な依頼にも関わらず、たくさんのご提案をいただけ幸甚に存じます。
素敵なデザインばかりで今後の勉強にもさせていただきました。
1つしか当選にできず、心苦しい思いです。
この度は誠にありがとうございました。
皆様の益々のご活躍を祈念いたします。

```html
<!DOCTYPE html>
<html lang="ja">
<head>
<meta charset="utf-8">
<title>星空MIDORI帖 タイトル案</title>
<link href="https://fonts.googleapis.com/css2?family=Noto+Sans+JP:wght@400;500;700;900&display=swap" rel="stylesheet">
<style>
  :root {
    --paper: #ffffff;
    --ink: #111111;
    --band-blue: #b9d5ef;
    --band-green: #a4d26a;
  }
  * { box-sizing: border-box; margin: 0; padding: 0; }
  html, body { width: 846px; height: 1200px; overflow: hidden; background: var(--paper); }
  body { position: relative; font-family: "Noto Sans JP", sans-serif; color: var(--ink); }

  .masthead {
    position: absolute;
    left: 34px;
    width: 778px;
    height: 333px;
    background: var(--band);
  }
  .masthead--blue { top: 90px; --band: var(--band-blue); }
  .masthead--green { top: 578px; --band: var(--band-green); }

  .masthead__title {
    position: absolute;
    left: 20px;
    top: 26px;
    white-space: nowrap;
    line-height: 1;
    font-size: 92px;
    font-weight: 700;
    letter-spacing: 0;
  }

  .articles {
    position: absolute;
    left: 0;
    bottom: 0;
    width: 334px;
    height: 132px;
    background: var(--paper);
    padding: 10px 12px;
  }
  .articles__label { font-size: 13px; font-weight: 700; margin-bottom: 4px; }
  .articles__list { list-style: none; font-size: 11.5px; line-height: 1.75; white-space: nowrap; }
  .articles__list li::before { content: "○"; }

  .issue {
    position: absolute;
    left: 384px;
    top: 172px;
    width: 394px;
    height: 36px;
    display: flex;
    align-items: flex-end;
    justify-content: flex-end;
  }
  .issue__date {
    background: var(--paper);
    height: 26px;
    padding: 0 14px;
    display: flex;
    align-items: center;
    font-size: 14px;
    font-weight: 500;
    white-space: nowrap;
  }
  .issue__date small { font-size: 10px; margin: 0 1px; }
  .issue__date .day { margin-left: 10px; }
  .issue__number {
    display: flex;
    align-items: baseline;
    font-size: 15px;
    font-weight: 700;
    padding: 0 12px 0 6px;
    line-height: 1;
  }
  .issue__number strong { font-size: 30px; font-weight: 900; letter-spacing: -1px; }

  .publisher {
    position: absolute;
    left: 398px;
    top: 216px;
    width: 370px;
  }
  .publisher__name { font-size: 15px; font-weight: 700; }
  .publisher__name span { margin-right: 10px; }
  .publisher__url { font-size: 15.5px; font-weight: 700; letter-spacing: 0.2px; margin-top: 2px; white-space: nowrap; }
  .offices { margin-top: 8px; font-size: 10px; line-height: 1.55; }
  .offices__row { display: grid; grid-template-columns: 44px 1fr 110px; }
</style>
</head>
<body>

  <section class="masthead masthead--blue">
    <h1 class="masthead__title">星空MIDORI帖</h1>

    <div class="articles">
      <p class="articles__label">主な記事</p>
      <ul class="articles__list">
        <li>脱炭素・SDGsからみた日本企業の技術ポテンシャル&gt;2面</li>
        <li>ブックステーション&gt;2-3面</li>
        <li>開発国から物申す～連載第13回～&gt;3面</li>
        <li>お家時間を充実させるおすすめグッズ&gt;4面</li>
      </ul>
    </div>

    <div class="issue">
      <p class="issue__date">2022<small>(令和4)</small>年<span class="day">6月15日</span></p>
      <p class="issue__number">第<strong>27</strong>号</p>
    </div>

    <div class="publisher">
      <p class="publisher__name"><span>発行</span>株式会社 青葉書房社</p>
      <p class="publisher__url">https://www.aobashobo-sample.co.jp/</p>
      <div class="offices">
        <p class="offices__row"><span>東　京</span><span>千代田区外松原3-5-8</span><span>TEL:03-4927-6830</span></p>
        <p class="offices__row"><span>大　阪</span><span>大阪市北区西桜台4-7-21</span><span>TEL:06-6718-2945</span></p>
        <p class="offices__row"><span>名古屋</span><span>刈谷市若草町5-14-3</span><span>TEL:0566-71-2049</span></p>
      </div>
    </div>
  </section>

  <section class="masthead masthead--green">
    <h1 class="masthead__title">星空MIDORI帖</h1>

    <div class="articles">
      <p class="articles__label">主な記事</p>
      <ul class="articles__list">
        <li>脱炭素・SDGsからみた日本企業の技術ポテンシャル&gt;2面</li>
        <li>ブックステーション&gt;2-3面</li>
        <li>開発国から物申す～連載第13回～&gt;3面</li>
        <li>お家時間を充実させるおすすめグッズ&gt;4面</li>
      </ul>
    </div>

    <div class="issue">
      <p class="issue__date">2022<small>(令和4)</small>年<span class="day">6月15日</span></p>
      <p class="issue__number">第<strong>27</strong>号</p>
    </div>

    <div class="publisher">
      <p class="publisher__name"><span>発行</span>株式会社 青葉書房社</p>
      <p class="publisher__url">https://www.aobashobo-sample.co.jp/</p>
      <div class="offices">
        <p class="offices__row"><span>東　京</span><span>千代田区外松原3-5-8</span><span>TEL:03-4927-6830</span></p>
        <p class="offices__row"><span>大　阪</span><span>大阪市北区西桜台4-7-21</span><span>TEL:06-6718-2945</span></p>
        <p class="offices__row"><span>名古屋</span><span>刈谷市若草町5-14-3</span><span>TEL:0566-71-2049</span></p>
      </div>
    </div>
  </section>

</body>
</html>
```